Business Card Design Project

Thornwick Property Management

Our Business is residential property management, we therefore need a card that displays a professional image, but is clear and concise, and easy to read
Updates

We are committed now guys and girls, loving what we are seeing so far! 

Target Market(s)

Landlords, Rental Property Owners

Industry/Entity Type

Residential

Requirements
Must have
• Dale Thornwick - Principal
Fiona Thornwick - Director (Property Management)

PO Box 817
Pellworth SA 5193

Dale: 0490 367 258
Fiona: 0490 723 519

www.thornwickpropertymanagement.com.au
admin@thornwickpropertymanagement.com.au

Nice to have
• I would like the card to be double sided, white background on the information side and then colour on the reverse, in blue or black and incorporating our logo

```html
<!DOCTYPE html>
<html lang="en">
<head>
<meta charset="utf-8">
<title>Thornwick Property Management – Business Card</title>
<link rel="stylesheet" href="https://fonts.googleapis.com/css2?family=Lato:wght@400;700&display=swap">
<style>
  :root {
    --page-bg: #e6e9eb;
    --card-white: #ffffff;
    --card-black: #141414;
    --card-black-light: #2b2b2b;
    --brand-blue: #1f74c4;
    --brand-blue-dark: #125a9e;
    --ink: #2a2a2a;
    --ink-soft: #4a4a4a;
    --deco-grey: #e4e4e4;
    --deco-grey-dark: #555555;
  }
  * { box-sizing: border-box; margin: 0; padding: 0; }
  html, body {
    width: 1200px;
    height: 960px;
    overflow: hidden;
    background: var(--page-bg);
    font-family: "Lato", Arial, sans-serif;
  }
  .stage {
    width: 1200px;
    height: 960px;
    display: flex;
    flex-direction: column;
    align-items: center;
    justify-content: center;
    gap: 60px;
  }
  .card {
    position: relative;
    width: 640px;
    height: 366px;
    border-radius: 4px;
    overflow: hidden;
    box-shadow: 0 6px 18px rgba(0, 0, 0, 0.18);
  }

  /* Information side */
  .card--front {
    background: var(--card-white);
    color: var(--ink);
    text-align: center;
    padding: 44px 40px 0;
  }
  .brand {
    display: flex;
    align-items: center;
    justify-content: center;
    gap: 14px;
  }
  .brand__mark {
    width: 40px;
    height: 40px;
    background: var(--brand-blue);
  }
  .brand__name {
    font-weight: 700;
    font-size: 30px;
    color: var(--ink-soft);
    letter-spacing: -0.3px;
  }
  .contact-row {
    font-size: 15px;
    color: var(--ink);
    padding: 10px 0 6px;
    border-bottom: 2px solid var(--brand-blue);
    white-space: nowrap;
  }
  .contact-row:first-of-type { margin-top: 36px; }
  .contact-row__name {
    font-size: 25px;
    letter-spacing: 0.2px;
  }
  .contact-row__sep { margin: 0 3px; }
  .details {
    margin-top: 12px;
    font-size: 15.5px;
    line-height: 1.45;
    color: var(--ink);
    position: relative;
    z-index: 1;
  }
  .details__web { font-weight: 700; font-size: 16px; }
  .front-deco {
    position: absolute;
    right: 0;
    bottom: 0;
    width: 170px;
    height: 130px;
    background: linear-gradient(135deg, transparent 30%, var(--deco-grey) 100%);
  }

  /* Reverse side */
  .card--back {
    background: radial-gradient(ellipse at 60% 30%, var(--card-black-light) 0%, var(--card-black) 70%);
    display: flex;
    align-items: center;
    justify-content: center;
  }
  .card--back .brand__name { color: var(--card-white); font-size: 34px; }
  .card--back .brand__mark { width: 46px; height: 46px; }
  .back-deco {
    position: absolute;
    right: 0;
    bottom: 14px;
    width: 190px;
    height: 60px;
    background: linear-gradient(90deg, transparent 0%, var(--deco-grey-dark) 100%);
  }
  .back-stripe {
    position: absolute;
    left: 0;
    right: 0;
    bottom: 0;
    height: 14px;
    background: linear-gradient(90deg, var(--brand-blue-dark), var(--brand-blue));
  }
</style>
</head>
<body>
<main class="stage">
  <section class="card card--front" aria-label="Business card, information side">
    <div class="brand">
      <span class="brand__mark"></span>
      <span class="brand__name">Thornwick Property Management</span>
    </div>
    <p class="contact-row">
      <span class="contact-row__name">DALE THORNWICK</span>
      <span class="contact-row__sep">|</span>Principal<span class="contact-row__sep">|</span>T: 0490 367 258
    </p>
    <p class="contact-row">
      <span class="contact-row__name">FIONA THORNWICK</span>
      <span class="contact-row__sep">|</span>Director (Property Management)<span class="contact-row__sep">|</span>T: 0490 723 519
    </p>
    <div class="details">
      <p>E: admin@thornwickpropertymanagement.com.au</p>
      <p>PO Box 817, Pellworth SA 5193</p>
      <p class="details__web">www.thornwickpropertymanagement.com.au</p>
    </div>
    <div class="front-deco" role="img" aria-label="Faint grey stepped corner decoration"></div>
  </section>

  <section class="card card--back" aria-label="Business card, reverse side">
    <div class="brand">
      <span class="brand__mark"></span>
      <span class="brand__name">Thornwick Property Management</span>
    </div>
    <div class="back-deco" role="img" aria-label="Grey stepped corner decoration"></div>
    <div class="back-stripe"></div>
  </section>
</main>
</body>
</html>
```